Business Card Design

Melodex Podcast

Industry/Entity Type

Business

Contact Information for Business Card

YOU ARE INVITED TO LISTEN
Stretch Every Idea
Award Winning Melodex Podcast
with Dr. Marla Quenby
www.drmarlaquenby-example.com

555-018-7364

```html
<!DOCTYPE html>
<html lang="en">
<head>
<meta charset="utf-8">
<title>Melodex Podcast – Business Card</title>
<link rel="stylesheet" href="https://fonts.googleapis.com/css2?family=Marcellus&family=Questrial&family=EB+Garamond:wght@500&family=Open+Sans:wght@400&display=swap">
<style>
  :root {
    --page-bg: #e4e4e4;
    --card-green-light: #cde58a;
    --card-green: #bcd96a;
    --card-green-deep: #aecd55;
    --olive: #5d6f30;
    --olive-text: #5a6a2f;
    --subtitle: #62803a;
    --white: #ffffff;
    --mic-light: #e2e4e4;
    --mic-mid: #a9acad;
    --mic-dark: #5c5f60;
  }
  * { margin: 0; padding: 0; box-sizing: border-box; }
  html, body {
    width: 1200px;
    height: 1000px;
    overflow: hidden;
    background: var(--page-bg);
  }
  .business-card {
    position: absolute;
    left: 176px;
    top: 261px;
    width: 840px;
    height: 490px;
    overflow: hidden;
    background: radial-gradient(ellipse at 35% 30%, var(--card-green-light) 0%, var(--card-green) 55%, var(--card-green-deep) 100%);
  }
  .invite-block {
    position: absolute;
    left: 20px;
    top: 66px;
    width: 470px;
    text-align: center;
    z-index: 2;
  }
  .invite-heading {
    font-family: "Marcellus", serif;
    font-weight: 400;
    font-size: 43px;
    line-height: 48px;
    color: var(--olive-text);
    letter-spacing: 1.5px;
  }
  .podcast-tagline {
    margin-top: 41px;
    font-family: "Questrial", sans-serif;
    font-size: 18px;
    line-height: 28px;
    color: var(--subtitle);
  }
  .host-name {
    margin-top: 29px;
    font-family: "EB Garamond", serif;
    font-weight: 500;
    font-size: 31px;
    color: var(--olive);
  }
  .contact-bar {
    position: absolute;
    left: 0;
    top: 373px;
    width: 456px;
    height: 58px;
    z-index: 2;
  }
  .contact-bar svg { position: absolute; inset: 0; }
  .contact-text {
    position: absolute;
    left: 35px;
    top: 0;
    height: 58px;
    display: flex;
    align-items: center;
    gap: 8px;
    font-family: "Open Sans", sans-serif;
    font-size: 16.5px;
    letter-spacing: -0.1px;
    color: var(--white);
    white-space: nowrap;
  }
  .contact-dot {
    width: 9px;
    height: 9px;
    border-radius: 50%;
    background: var(--white);
    flex: none;
  }
  .microphone-photo {
    position: absolute;
    left: 486px;
    top: 54px;
    width: 306px;
    height: 436px;
    border-radius: 150px 150px 0 0;
    background: linear-gradient(120deg, var(--mic-light) 0%, var(--mic-mid) 50%, var(--mic-dark) 100%);
    z-index: 1;
  }
</style>
</head>
<body>
  <main class="business-card">
    <section class="invite-block">
      <h1 class="invite-heading">YOU ARE INVITED<br>TO LISTEN</h1>
      <p class="podcast-tagline">Stretch Every Idea Award Winning<br>Melodex Podcast with</p>
      <p class="host-name">Dr. Marla Quenby</p>
    </section>

    <div class="contact-bar">
      <svg width="456" height="58" viewBox="0 0 456 58" aria-hidden="true">
        <path d="M0 0 H428 Q440 0 446 10 L456 29 L446 48 Q440 58 428 58 H0 Z" fill="var(--olive)"/>
      </svg>
      <p class="contact-text">
        <span class="contact-web">www.drmarlaquenby-example.com</span>
        <span class="contact-dot"></span>
        <span class="contact-phone">555-018-7364</span>
      </p>
    </div>

    <div class="microphone-photo" role="img" aria-label="Photo of a chrome vintage studio microphone"></div>
  </main>
</body>
</html>
```